Zielgruppe
Wir schreiben ebooks und haben verschiedene Zielgruppen. In diesem Projekt sind es Scherheitsbewusste Eigenheimbesitzer, welche sich über die aktiven und passiven Möglichkeiten zum Einbruchschutz informieren möchten
Aufgabenstellung
Es ist ein Tatgeber zur Vermeidung von Einbrüchen. Dem Design für unser Cover sind keine Grenzen gesetzt. Es soll ansprechend sein, und Lust auf mehr Content machen.

```html
<!DOCTYPE html>
<html lang="de">
<head>
<meta charset="UTF-8">
<title>Vermeidung von Einbrüchen – Buchcover</title>
<link rel="stylesheet" href="https://fonts.googleapis.com/css2?family=Playfair+Display:wght@700;900&family=Open+Sans:wght@500&display=swap">
<style>
  :root {
    --page-bg: #ededed;
    --navy-deep: #141947;
    --navy: #1e2570;
    --navy-bright: #2b3aa6;
    --wood-dark: #3b1c0f;
    --wood-warm: #c46d32;
    --wood-light: #f2b56c;
    --brick: #8a4a33;
    --floor-dark: #120c12;
    --title-white: #ffffff;
    --author-orange: #e0953f;
  }
  * { margin: 0; padding: 0; box-sizing: border-box; }
  html, body {
    width: 1200px;
    height: 2289px;
    overflow: hidden;
    background: var(--page-bg);
  }
  .canvas {
    position: relative;
    width: 1200px;
    height: 2289px;
    display: flex;
    align-items: center;
    justify-content: center;
  }
  .book-cover {
    position: relative;
    width: 1080px;
    height: 1526px;
    overflow: hidden;
    box-shadow: 0 6px 24px rgba(0,0,0,0.18);
  }
  .cover-photo {
    position: absolute;
    inset: 0;
    background:
      /* dark floor along the bottom */
      linear-gradient(180deg, rgba(18,12,18,0) 72%, rgba(18,12,18,0.9) 92%, var(--floor-dark) 100%),
      /* dark hooded figure, lower right */
      radial-gradient(ellipse 48% 42% at 70% 68%, rgba(20,22,70,0.95) 0%, rgba(20,22,70,0.6) 55%, rgba(20,22,70,0) 100%),
      /* lit blue brick wall, centre */
      radial-gradient(ellipse 16% 38% at 52% 50%, rgba(50,72,190,0.75) 0%, rgba(50,72,190,0) 100%),
      /* window frame and warm interior light, left */
      linear-gradient(90deg,
        var(--wood-dark) 0%,
        #6b3418 3%,
        var(--wood-warm) 7%,
        var(--wood-light) 11%,
        #f7d9a6 13%,
        var(--wood-warm) 17%,
        #9c5022 22%,
        var(--wood-warm) 28%,
        var(--wood-light) 32%,
        var(--wood-warm) 36%,
        var(--brick) 42%,
        #3a3f95 50%,
        var(--navy) 62%,
        var(--navy-deep) 100%);
  }
  .cover-text {
    position: absolute;
    inset: 0;
    text-align: center;
    color: var(--title-white);
    font-family: "Playfair Display", Georgia, serif;
  }
  .kicker {
    position: absolute;
    top: 38px;
    left: 0; right: 0;
    font-size: 33px;
    font-weight: 700;
    letter-spacing: -0.5px;
  }
  .title-line {
    position: absolute;
    left: 0; right: 0;
    font-weight: 900;
    line-height: 1;
    letter-spacing: -3px;
  }
  .title-main { top: 112px; font-size: 134px; }
  .title-joiner { top: 242px; font-size: 72px; font-weight: 700; letter-spacing: 0; }
  .title-end { top: 332px; font-size: 134px; }
  .author-name {
    position: absolute;
    top: 1354px;
    left: 0; right: 0;
    text-align: center;
    font-family: "Open Sans", Arial, sans-serif;
    font-weight: 500;
    font-size: 50px;
    letter-spacing: 12px;
    color: var(--author-orange);
  }
</style>
</head>
<body>
<div class="canvas">
  <section class="book-cover">
    <div class="cover-photo" role="img" aria-label="Foto: vermummter Einbrecher in dunklem Kapuzenpulli hebelt nachts mit einem Brecheisen ein beleuchtetes Holzfenster an einer blauen Backsteinwand auf"></div>
    <div class="cover-text">
      <p class="kicker">Es ist ein Ratgeber zur</p>
      <h1>
        <span class="title-line title-main">Vermeidung</span>
        <span class="title-line title-joiner">von</span>
        <span class="title-line title-end">Einbrüchen</span>
      </h1>
      <p class="author-name">Autorenname</p>
    </div>
  </section>
</div>
</body>
</html>
```